Bright Harbor Realty

We need a good looking flyer for our real estate company to impress people who are considering to sell their homes for as low as 1.5% listing commission. Please see flyer examples for reference.
555-318-4906

```html
<!DOCTYPE html>
<html lang="en">
<head>
<meta charset="utf-8">
<title>Bright Harbor Realty — Just Sold Flyer</title>
<link href="https://fonts.googleapis.com/css2?family=Bebas+Neue&family=Open+Sans:wght@400;600;700&display=swap" rel="stylesheet">
<style>
  :root {
    --brand-blue: #0a4fa3;
    --brand-red: #e4222b;
    --white: #ffffff;
    --ink: #2b2b2b;
    --page-bg: #e6e4e1;
    --frame-dark: #3a3330;
  }
  * { box-sizing: border-box; margin: 0; padding: 0; }
  html, body { width: 1200px; height: 1200px; overflow: hidden; }
  body { background: var(--page-bg); font-family: "Open Sans", sans-serif; }

  .flyer {
    position: absolute; left: 160px; top: 30px;
    width: 880px; height: 1140px;
    background: var(--white);
    box-shadow: 0 4px 14px rgba(0,0,0,.18);
  }
  .listings-panel {
    position: absolute; left: 0; top: 0; width: 880px; height: 895px;
    background: var(--brand-blue);
  }

  .headline-bar {
    position: absolute; left: 49px; top: 49px; width: 783px; height: 122px;
    display: flex; background: var(--white);
  }
  .headline-bar__title {
    width: 392px; background: var(--brand-red); color: var(--white);
    font-family: "Bebas Neue", sans-serif; font-weight: 400; font-size: 94px; letter-spacing: 2px;
    display: flex; align-items: center; justify-content: center; padding-top: 8px;
  }
  .headline-bar__tagline {
    flex: 1; color: var(--brand-blue); font-weight: 700; font-size: 22px; line-height: 1.3;
    display: flex; align-items: center; justify-content: center; text-align: center;
  }

  .property-card { position: absolute; width: 380px; text-align: center; color: var(--white); }
  .property-card__photo {
    width: 380px; height: 170px; border: 2px solid var(--white);
  }
  .property-card__title,
  .property-card__detail {
    font-size: 17px; white-space: nowrap; letter-spacing: -0.2px;
  }
  .property-card__title { font-weight: 700; line-height: 1.1; margin-top: 4px; }
  .property-card__detail { font-weight: 400; line-height: 1.25; }

  .photo--sky-tan   { background: linear-gradient(180deg, #b9cde0 0%, #b69574 55%, #8d8a83 100%); }
  .photo--sky-lawn  { background: linear-gradient(180deg, #8fc1ea 0%, #cfe3ef 45%, #6ea944 100%); }
  .photo--grey-lawn { background: linear-gradient(180deg, #c6dcef 0%, #8e8f8c 55%, #5f9a3a 100%); }
  .photo--cream     { background: linear-gradient(180deg, #7fb1de 0%, #ece7d6 45%, #78a85a 100%); }
  .photo--white-two { background: linear-gradient(180deg, #8bb7e4 0%, #ece7df 50%, #5f9146 100%); }
  .photo--olive     { background: linear-gradient(180deg, #9fc3df 0%, #a7a04c 50%, #558a3a 100%); }

  .agent-photo {
    position: absolute; left: 49px; top: 945px; width: 147px; height: 147px;
    border: 7px solid var(--frame-dark);
    background: linear-gradient(180deg, #b7aba3 0%, #8a7c73 55%, #25211f 100%);
  }
  .brokerage-name {
    position: absolute; left: 218px; top: 985px; width: 160px;
    display: flex; flex-direction: column; align-items: center; gap: 10px;
    color: var(--brand-blue); font-weight: 700; font-size: 19px; line-height: 1.15; text-align: center;
  }
  .brokerage-name__mark { width: 26px; height: 26px; background: var(--brand-blue); }

  .commission-banner {
    position: absolute; left: 403px; top: 944px; width: 477px; height: 74px;
    background: var(--brand-red); color: var(--white);
    display: flex; align-items: center; padding-left: 46px; gap: 12px;
    white-space: nowrap;
  }
  .commission-banner__rate { font-family: "Bebas Neue", sans-serif; font-size: 86px; line-height: 1; padding-top: 12px; }
  .commission-banner__label { font-family: "Bebas Neue", sans-serif; font-size: 40px; line-height: .9; padding-top: 6px; }
  .commission-banner__sub { font-size: 19px; line-height: 1; }

  .agent-contact { position: absolute; left: 455px; top: 1026px; color: var(--ink); white-space: nowrap; }
  .agent-contact__name { font-weight: 700; font-size: 34px; line-height: 1.1; }
  .agent-contact__details { font-weight: 700; font-size: 19px; margin-top: 2px; }
  .agent-contact__divider { font-weight: 400; margin: 0 6px; }
</style>
</head>
<body>
  <main class="flyer">
    <section class="listings-panel">
      <header class="headline-bar">
        <h1 class="headline-bar__title">JUST SOLD</h1>
        <p class="headline-bar__tagline">List For 1.5% Commission,<br>Still Receive Top Marketing!</p>
      </header>

      <article class="property-card" style="left:49px; top:195px;">
        <div class="property-card__photo photo--sky-tan" role="img" aria-label="Photo of two tan two-story townhomes with parked cars"></div>
        <h2 class="property-card__title">Lorem Ipsum Dolor Sit Amet</h2>
        <p class="property-card__detail">Duo sadipscing odio in feugiat no iusto dolore</p>
      </article>
      <article class="property-card" style="left:453px; top:195px;">
        <div class="property-card__photo photo--sky-lawn" role="img" aria-label="Photo of a light blue single-story home with palm trees and lawn"></div>
        <h2 class="property-card__title">Lorem Ipsum Dolor Sit Amet</h2>
        <p class="property-card__detail">Duo sadipscing odio in feugiat no iusto dolore</p>
      </article>
      <article class="property-card" style="left:49px; top:423px;">
        <div class="property-card__photo photo--grey-lawn" role="img" aria-label="Photo of a grey stone-front ranch home with a wide lawn"></div>
        <h2 class="property-card__title">Lorem Ipsum Dolor Sit Amet</h2>
        <p class="property-card__detail">Duo sadipscing odio in feugiat no iusto dolore</p>
      </article>
      <article class="property-card" style="left:453px; top:423px;">
        <div class="property-card__photo photo--cream" role="img" aria-label="Photo of a cream single-story home with carport and mailbox"></div>
        <h2 class="property-card__title">Lorem Ipsum Dolor Sit Amet</h2>
        <p class="property-card__detail">Duo sadipscing odio in feugiat no iusto dolore</p>
      </article>
      <article class="property-card" style="left:49px; top:650px;">
        <div class="property-card__photo photo--white-two" role="img" aria-label="Photo of a white two-story home with a double garage and trees"></div>
        <h2 class="property-card__title">Lorem Ipsum Dolor Sit Amet</h2>
        <p class="property-card__detail">Duo sadipscing odio in feugiat no iusto dolore</p>
      </article>
      <article class="property-card" style="left:453px; top:650px;">
        <div class="property-card__photo photo--olive" role="img" aria-label="Photo of an olive green home with white garage door and tropical plants"></div>
        <h2 class="property-card__title">Lorem Ipsum Dolor Sit Amet</h2>
        <p class="property-card__detail">Duo sadipscing odio in feugiat no iusto dolore</p>
      </article>
    </section>

    <div class="agent-photo" role="img" aria-label="Agent headshot portrait"></div>

    <div class="brokerage-name">
      <span class="brokerage-name__mark"></span>
      <span>Bright Harbor Realty</span>
    </div>

    <div class="commission-banner">
      <span class="commission-banner__rate">1.5%</span>
      <div>
        <div class="commission-banner__label">LISTING COMMISSION</div>
        <div class="commission-banner__sub">Still Receive Top Marketing!</div>
      </div>
    </div>

    <div class="agent-contact">
      <p class="agent-contact__name">My Name</p>
      <p class="agent-contact__details">555-318-4906<span class="agent-contact__divider">|</span>www.BrightHarborRealty.us</p>
    </div>
  </main>
</body>
</html>
```